Business Card/ Car Magnet/ Polo Shirt/ Envelope/ Letterhead Design Project
Birchmont Property Valuations, LLC.
Business Card/ Car Magnet/ Polo Shirt/ Envelope/ Letterhead Design Project - Real Estate
Creative Brief
Professional
Gus Talbottine
State Certified Residential Real Estate Appraiser
14 Coldmeadow Ln Sewell, NJ 08080
gtalbottine@birchmontvaluations.example
valuemarkhq.example
NJ- 57RC00913400 PA- RL284615 DE- X2-0000317
Please be creative...
gust1983 gust1983
Hello, Just wanted to clarify some of the common questions asked so far. The colors to incorporate would be blue, green and white (unless of course you would like to incorporate other colors for creativity) . please feel free to incorporate them any way you see fit. The polo shirts will be done on white, black and royal blue shirts. Please be as creative as you like. Thanks you for your efforts and for participating! Please reply back with any further questions. Thanks! BPV

```html
<!DOCTYPE html>
<html lang="en">
<head>
<meta charset="utf-8">
<title>Birchmont Property Valuations — Business Card</title>
<link href="https://fonts.googleapis.com/css2?family=Cinzel:wght@500;700&family=Open+Sans:wght@400;600;700&display=swap" rel="stylesheet">
<style>
  :root{
    --bg:#e9eaec;
    --card:#ffffff;
    --blue:#1c5aa6;
    --blue-light:#2f86d6;
    --green:#5fae2e;
    --green-light:#9ccf3a;
    --ink:#3d4450;
    --muted:#6d7480;
  }
  *{margin:0;padding:0;box-sizing:border-box}
  html,body{width:1200px;height:939px;overflow:hidden;background:var(--bg)}
  body{font-family:"Open Sans",Arial,sans-serif;position:relative}
  .card{position:absolute;width:500px;height:286px;background:var(--card);
        box-shadow:0 10px 28px rgba(0,0,0,.16);overflow:hidden}
  .card--front{left:70px;top:330px}
  .card--back{left:630px;top:330px}
  .card--back::after{content:"";position:absolute;left:0;right:0;bottom:0;height:6px;
        background:linear-gradient(90deg,var(--green),var(--blue-light))}

  .wordmark{position:absolute;left:34px;top:24px}
  .wordmark__name{font-family:"Cinzel",Georgia,serif;font-weight:700;font-size:44px;
        color:var(--blue);letter-spacing:3px;line-height:1}
  .wordmark__company{font-size:8.5px;font-weight:600;color:var(--green);letter-spacing:.6px;
        text-transform:uppercase;margin-top:5px;padding-top:4px;border-top:1px solid var(--green);display:inline-block}

  .person{position:absolute;left:34px;top:102px}
  .person__name{font-weight:700;font-size:15px;color:var(--green);line-height:1.3}
  .person__title{font-size:10.5px;color:var(--muted);margin-top:1px;line-height:1.3}

  .contacts{position:absolute;left:34px;top:146px;list-style:none;font-size:9.5px;color:var(--ink)}
  .contacts li{display:flex;align-items:center;gap:6px;height:15px;white-space:nowrap}
  .contacts svg{width:9px;height:9px;flex:none}

  .licenses{position:absolute;left:34px;top:226px;font-size:8.5px;color:var(--muted);
        line-height:13px;white-space:nowrap}
  .licenses span{margin-right:8px}

  .swoosh{position:absolute;left:0;top:0;width:500px;height:286px}

  .back-mark{position:absolute;left:0;right:0;top:104px;text-align:center}
  .back-mark__row{display:inline-flex;align-items:center;gap:10px}
  .back-mark__name{font-family:"Cinzel",Georgia,serif;font-weight:700;font-size:40px;color:var(--blue);letter-spacing:3px;line-height:1}
  .back-mark__dot{width:26px;height:26px;border-radius:50%;border:3px solid var(--green)}
  .back-mark__company{font-size:8.5px;font-weight:600;color:var(--green);letter-spacing:.6px;
        text-transform:uppercase;margin-top:6px}
</style>
</head>
<body>

<section class="card card--front" aria-label="Business card front">
  <svg class="swoosh" viewBox="0 0 500 286" aria-hidden="true">
    <defs>
      <linearGradient id="blueBand" x1="0" y1="0" x2="1" y2="0">
        <stop offset="0" stop-color="#2f86d6"/><stop offset="1" stop-color="#1c5aa6"/>
      </linearGradient>
      <linearGradient id="greenBand" x1="0" y1="0" x2="1" y2="0">
        <stop offset="0" stop-color="#9ccf3a"/><stop offset="1" stop-color="#5fae2e"/>
      </linearGradient>
    </defs>
    <path d="M250 286 C330 280 390 250 430 180 C455 135 475 118 500 112 L500 286 Z" fill="url(#blueBand)"/>
    <path d="M200 286 C300 282 370 262 410 220 C440 190 470 175 500 178 L500 206 C470 204 445 218 420 240 C380 272 320 286 260 286 Z" fill="url(#greenBand)"/>
    <path d="M236 286 C320 280 378 258 414 222 C444 194 470 184 500 186 L500 196 C470 196 446 208 420 232 C384 264 330 286 270 286 Z" fill="#ffffff"/>
    <circle cx="418" cy="178" r="44" fill="#ffffff"/>
    <circle cx="418" cy="178" r="34" fill="none" stroke="#1c5aa6" stroke-width="3"/>
  </svg>

  <div class="wordmark">
    <div class="wordmark__name">BPV</div>
    <div class="wordmark__company">Birchmont Property Valuations, LLC.</div>
  </div>

  <div class="person">
    <div class="person__name">Gus Talbottine</div>
    <div class="person__title">State Certified Residential Real Estate Appraiser</div>
  </div>

  <ul class="contacts">
    <li><svg viewBox="0 0 10 10"><path d="M5 0a3.5 3.5 0 0 0-3.5 3.5C1.5 6 5 10 5 10s3.5-4 3.5-6.5A3.5 3.5 0 0 0 5 0zm0 5a1.4 1.4 0 1 1 0-2.8A1.4 1.4 0 0 1 5 5z" fill="#1c5aa6"/></svg>14 Coldmeadow Ln Sewell, NJ 08080</li>
    <li><svg viewBox="0 0 10 10"><path d="M2 0l2 2.5-1 1.2c.6 1.3 1.7 2.4 3 3l1.2-1L10 8l-1.5 2C4 10 0 6 0 1.5z" fill="#1c5aa6"/></svg>T. 012 345 6789</li>
    <li><svg viewBox="0 0 10 10"><rect x="0" y="2" width="10" height="6.5" rx="1" fill="#1c5aa6"/><path d="M0.5 2.5L5 6l4.5-3.5" stroke="#fff" fill="none" stroke-width="1"/></svg>gtalbottine@birchmontvaluations.example</li>
    <li><svg viewBox="0 0 10 10"><circle cx="5" cy="5" r="4.4" fill="none" stroke="#1c5aa6" stroke-width="1.2"/><path d="M0.6 5h8.8M5 0.6c-2.4 2.6-2.4 6.2 0 8.8M5 0.6c2.4 2.6 2.4 6.2 0 8.8" stroke="#1c5aa6" fill="none" stroke-width=".8"/></svg>valuemarkhq.example</li>
  </ul>

  <div class="licenses">
    <span>NJ- 57RC00913400</span><span>PA- RL284615</span><span>DE- X2-0000317</span>
  </div>
</section>

<section class="card card--back" aria-label="Business card back">
  <div class="back-mark">
    <div class="back-mark__row">
      <span class="back-mark__name">BPV</span>
      <span class="back-mark__dot"></span>
    </div>
    <div class="back-mark__company">Birchmont Property Valuations, LLC.</div>
  </div>
</section>

</body>
</html>
```